Solvane Vitamins

I am reaching out to discuss a design project for a food supplement line for my company, Solvane Pharma GmBH. I am looking for a design that is colorful, creative, consistent, and indicative of each product. Initially, we have two items in our product range:
1. Folic Acid 400 with B12+B6 (Box)
2. Vitamin D3 50,000 IU (Label)
I have attached the source files from another company for each item, including the die cuts, so feel free to change the logo and address and come up with a new theme.
The new address is: Quellmarkerstr 27 .36091 Fulda, Germany

Target Market(s)

Middle East

Industry/Entity Type

Vitamins

Font styles to use
Sans Serif

Colors
0054AA
0677BA
7BADD7
CADEEF
E8F1F8
6B429C
8869AF
B7A5CE
E3DAEB
F3F0F8

Requirements
Must have
• Flores and photos to iditify the product

```html
<!DOCTYPE html>
<html lang="en">
<head>
<meta charset="utf-8">
<title>Solvane Vitamins – Folic Acid Box &amp; Vitamin D3 Label</title>
<link href="https://fonts.googleapis.com/css2?family=Nunito:ital,wght@0,700;0,800;0,900;1,900&family=Roboto+Condensed:wght@400;500&family=Roboto:wght@400;500&display=swap" rel="stylesheet">
<style>
  :root {
    --bg: #eeeeec;
    --panel: #ffffff;
    --ink: #1c1c1c;
    --blue-900: #0054AA;
    --blue-700: #0677BA;
    --blue-400: #7BADD7;
    --blue-200: #CADEEF;
    --blue-50: #E8F1F8;
    --purple-900: #6B429C;
    --purple-700: #8869AF;
    --purple-400: #B7A5CE;
    --purple-200: #E3DAEB;
    --purple-50: #F3F0F8;
    --flag-black: #111111;
    --flag-red: #dd1f26;
    --flag-gold: #f7c600;
  }
  * { margin: 0; padding: 0; box-sizing: border-box; }
  html, body { width: 1200px; height: 1070px; overflow: hidden; }
  body { background: var(--bg); font-family: "Nunito", sans-serif; color: var(--ink); position: relative; }

  .pack { position: absolute; box-shadow: 0 4px 14px rgba(0,0,0,.12); }
  .box-front { left: 80px; top: 247px; width: 470px; height: 725px; background: linear-gradient(180deg, var(--panel), var(--purple-50)); }
  .bottle-label { left: 670px; top: 318px; width: 468px; height: 622px; background: linear-gradient(180deg, var(--panel), var(--blue-50)); }

  .band { position: absolute; }
  .box-front .band-top { left: 18px; top: 9px; width: 420px; height: 235px; background: linear-gradient(120deg, var(--purple-700), var(--purple-900)); }
  .box-front .band-bottom { left: 8px; top: 591px; width: 437px; height: 126px; background: linear-gradient(120deg, var(--purple-900), var(--purple-700)); }
  .bottle-label .band-top { left: 24px; top: 3px; width: 426px; height: 312px; background: linear-gradient(125deg, var(--blue-400) 0%, var(--blue-700) 45%, var(--blue-900) 100%); }
  .bottle-label .band-bottom { left: 0; top: 559px; width: 468px; height: 40px; background: linear-gradient(90deg, var(--blue-700), var(--blue-900)); border-top: 3px solid var(--blue-400); }

  .product-photo { position: absolute; }
  .box-front .product-photo { left: 330px; top: 372px; width: 118px; height: 188px; border-radius: 14px; background: linear-gradient(160deg, var(--purple-200), var(--purple-400)); }
  .bottle-label .product-photo { left: 44px; top: 26px; width: 150px; height: 150px; border-radius: 50%; background: radial-gradient(circle at 40% 35%, var(--blue-50), var(--blue-200) 60%, var(--blue-400)); }

  .brand { position: absolute; font-weight: 900; font-size: 42px; letter-spacing: .5px; line-height: 1; color: #fff; }
  .box-front .brand { left: 238px; top: 42px; }
  .bottle-label .brand { left: 247px; top: 62px; }

  .product-name { position: absolute; font-weight: 900; color: #fff; line-height: 1; }
  .box-front .product-name { left: 60px; top: 168px; font-size: 48px; }
  .bottle-label .product-name { left: 68px; top: 216px; font-size: 56px; }

  .dose { position: absolute; font-weight: 900; line-height: 1; }
  .box-front .dose { left: 28px; top: 262px; font-size: 44px; color: var(--purple-900); font-style: italic; }
  .bottle-label .dose { left: 29px; top: 326px; font-size: 50px; color: var(--blue-900); }

  .supplement { position: absolute; font-family: "Roboto Condensed", sans-serif; font-weight: 500; }
  .box-front .supplement { left: 30px; top: 310px; font-size: 14px; }
  .bottle-label .supplement { left: 30px; top: 390px; font-size: 17px; }

  .count-pill { position: absolute; border-radius: 30px; display: flex; align-items: center; justify-content: center; font-weight: 900; color: var(--ink); }
  .box-front .count-pill { left: 316px; top: 266px; width: 100px; height: 44px; font-size: 34px; background: linear-gradient(90deg, var(--purple-400), var(--purple-200)); }
  .bottle-label .count-pill { left: 329px; top: 328px; width: 97px; height: 54px; font-size: 28px; background: linear-gradient(90deg, var(--blue-400), var(--blue-200)); }

  .count-unit { position: absolute; font-weight: 800; }
  .box-front .count-unit { left: 316px; top: 314px; width: 100px; text-align: center; font-size: 19px; }
  .bottle-label .count-unit { left: 318px; top: 390px; width: 120px; text-align: center; font-family: "Roboto Condensed", sans-serif; font-weight: 500; font-size: 10px; }

  .extra { position: absolute; left: 28px; top: 384px; font-size: 20px; font-weight: 900; font-style: italic; color: var(--purple-900); }
  .net-weight { position: absolute; left: 36px; top: 412px; font-size: 11px; font-weight: 900; font-style: italic; }

  .claims { position: absolute; left: 26px; top: 474px; list-style: none; font-family: "Roboto Condensed", sans-serif; font-size: 16px; line-height: 31px; }
  .claims li::before { content: ""; display: inline-block; width: 6px; height: 6px; border-radius: 50%; background: var(--purple-700); margin-right: 8px; vertical-align: middle; }

  .origin { position: absolute; display: flex; align-items: center; gap: 6px; font-family: "Roboto", sans-serif; }
  .box-front .origin { left: 20px; top: 616px; font-size: 14px; color: var(--purple-50); }
  .bottle-label .origin { left: 28px; top: 432px; font-size: 12px; color: #333; }
  .flag { border-radius: 50%; overflow: hidden; display: block; }

  .address { position: absolute; font-family: "Roboto", sans-serif; font-size: 11px; }
  .box-front .address { left: 22px; top: 690px; color: var(--purple-50); }
  .bottle-label .address { left: 28px; top: 573px; color: var(--blue-50); }

  .tagline { position: absolute; left: 32px; top: 488px; font-size: 22px; font-weight: 800; color: var(--blue-700); line-height: 30px; }

  .batch-info { position: absolute; display: flex; font-family: "Roboto", sans-serif; }
  .batch-info span { writing-mode: vertical-rl; transform: rotate(180deg); }
  .box-front .batch-info { left: 344px; top: 610px; font-size: 11px; color: var(--purple-50); gap: 17px; }
  .bottle-label .batch-info { left: 366px; top: 470px; font-size: 12px; color: #222; gap: 13px; }
</style>
</head>
<body>

  <section class="pack box-front" aria-label="Folic Acid box front">
    <div class="band band-top"></div>
    <div class="brand">Solvane</div>
    <h1 class="product-name">Folic Acid</h1>
    <div class="dose">400 µg</div>
    <div class="supplement">Dietary Supplement</div>
    <div class="count-pill">30</div>
    <div class="count-unit">Tablets</div>
    <div class="extra">with VITAMIN B12 &amp; B6</div>
    <div class="net-weight">Net weigth: 3.6 gr</div>
    <div class="product-photo" role="img" aria-label="Photo of fresh leafy greens and folate-rich foods"></div>
    <ul class="claims">
      <li>Made to High Standards of Quality Control</li>
      <li>No Artificial Colours or Preservatives</li>
      <li>Suitable for Vegans</li>
    </ul>
    <div class="band band-bottom"></div>
    <div class="origin">
      <svg class="flag" width="48" height="48" viewBox="0 0 48 48" aria-hidden="true">
        <rect width="48" height="16" fill="var(--flag-black)"/>
        <rect y="16" width="48" height="16" fill="var(--flag-red)"/>
        <rect y="32" width="48" height="16" fill="var(--flag-gold)"/>
      </svg>
      <span>Made in Germany</span>
    </div>
    <div class="batch-info"><span>Batch No:</span><span>Mfg. Date:</span><span>Exp. Date:</span></div>
    <div class="address">Solvane Pharma GmBH · Quellmarkerstr 27 .36091 Fulda, Germany</div>
  </section>

  <section class="pack bottle-label" aria-label="Vitamin D3 bottle label">
    <div class="band band-top"></div>
    <div class="product-photo" role="img" aria-label="Photo of golden softgel capsules in sunlight"></div>
    <div class="brand">Solvane</div>
    <h1 class="product-name">Vitamin D3</h1>
    <div class="dose">50,000 IU</div>
    <div class="supplement">Dietary Supplement</div>
    <div class="count-pill">120</div>
    <div class="count-unit">SOFTGEL CAPSULES</div>
    <div class="origin">
      <svg class="flag" width="38" height="38" viewBox="0 0 48 48" aria-hidden="true">
        <rect width="48" height="16" fill="var(--flag-black)"/>
        <rect y="16" width="48" height="16" fill="var(--flag-red)"/>
        <rect y="32" width="48" height="16" fill="var(--flag-gold)"/>
      </svg>
      <span>Made in Germany</span>
    </div>
    <p class="tagline">Supports healthy bones &amp;<br>the immune system</p>
    <div class="batch-info"><span>Batch No.:</span><span>Mfg. Date:</span><span>Exp. Date:</span></div>
    <div class="band band-bottom"></div>
    <div class="address">Solvane Pharma GmBH · Quellmarkerstr 27 .36091 Fulda, Germany</div>
  </section>

</body>
</html>
```